Need business cards for our e-assessment business

We need professional looking business cards for our e-assessment business based in Europe. Our company is called Velnor.

You can just use sample name and addresses.

The colours we use are:

#70abe4 (blue)
#FF6600 (orange)

The back side should say: E-assessment made easy

This is the print-shop we are using. Please look at the link for info about formats: http://nl.printqet.com/help/faq/using-my-own-artwork.html

Target Market(s)

Target market is education and large corporations

Industry/Entity Type

Business

```html
<!DOCTYPE html>
<html lang="en">
<head>
<meta charset="utf-8">
<title>Velnor business cards</title>
<link rel="stylesheet" href="https://fonts.googleapis.com/css2?family=Open+Sans:wght@400;600;700&display=swap">
<style>
  :root {
    --orange: #f26722;
    --blue: #70abe4;
    --ink: #3a3a3c;
    --text: #333333;
    --paper: #ffffff;
    --backdrop: #e9e6e1;
  }
  * { margin: 0; padding: 0; box-sizing: border-box; }
  html, body { width: 1200px; height: 1019px; overflow: hidden; }
  body {
    background: var(--backdrop);
    font-family: "Open Sans", Arial, sans-serif;
    position: relative;
  }
  .card {
    position: absolute;
    top: 200px;
    width: 400px;
    height: 618px;
    overflow: hidden;
    box-shadow: 0 10px 30px rgba(0,0,0,0.18);
  }
  .card-front { left: 160px; background: var(--paper); }
  .card-back { left: 640px; background: var(--orange); }

  .edge-bar { position: absolute; left: 0; background: var(--orange); }
  .edge-bar.top { top: 0; width: 62px; height: 112px; }
  .edge-bar.middle { top: 124px; width: 44px; height: 168px; }
  .edge-bar.bottom { top: 304px; width: 26px; height: 314px; }

  .brand {
    position: absolute;
    top: 52px;
    right: 36px;
    display: flex;
    align-items: center;
    gap: 14px;
  }
  .brand-dot {
    width: 66px; height: 66px;
    border-radius: 50%;
    background: var(--orange);
  }
  .brand-name {
    font-size: 56px;
    font-weight: 600;
    color: var(--ink);
    letter-spacing: -1px;
    line-height: 1;
  }

  .person { position: absolute; left: 70px; top: 250px; }
  .person-name { font-size: 26px; font-weight: 700; color: var(--orange); line-height: 1.1; }
  .person-role { font-size: 19px; color: var(--text); margin-top: 2px; }

  .contact-list {
    position: absolute;
    left: 70px; top: 350px;
    list-style: none;
    font-size: 16.5px;
    color: var(--text);
    line-height: 1.45;
  }
  .contact-list li { display: flex; align-items: flex-start; gap: 10px; }
  .contact-list svg { flex: none; width: 16px; height: 16px; margin-top: 4px; fill: var(--orange); }
  .contact-list .handle-mark { flex: none; width: 12px; height: 12px; margin: 6px 2px 0; background: var(--blue); }

  .back-disc {
    position: absolute;
    left: 70px; top: 150px;
    width: 260px; height: 260px;
    border-radius: 50%;
    background: var(--paper);
    display: flex; flex-direction: column; align-items: center; justify-content: center;
    gap: 6px;
  }
  .back-brand { font-size: 46px; font-weight: 600; color: var(--orange); letter-spacing: -1px; line-height: 1; }
  .back-tagline { font-size: 15px; font-weight: 600; color: var(--blue); }
  .web-address {
    position: absolute;
    left: 0; right: 0; bottom: 48px;
    text-align: center;
    font-size: 21px; font-weight: 700;
    color: var(--paper);
  }
</style>
</head>
<body>
  <section class="card card-front" aria-label="Business card front">
    <div class="edge-bar top"></div>
    <div class="edge-bar middle"></div>
    <div class="edge-bar bottom"></div>

    <div class="brand">
      <div class="brand-dot"></div>
      <div class="brand-name">velnor</div>
    </div>

    <div class="person">
      <div class="person-name">Maren Holtvik</div>
      <div class="person-role">Co-founder / CEO</div>
    </div>

    <ul class="contact-list">
      <li>
        <svg viewBox="0 0 16 16" aria-hidden="true"><path d="M1 6c0-3 3-4 7-4s7 1 7 4l-3 1-1-2H5L4 7 1 6zm3 2h8l2 6H2l2-6zm4 1.5a2 2 0 100 4 2 2 0 000-4z"/></svg>
        +31 (0)30 555 0182
      </li>
      <li>
        <svg viewBox="0 0 16 16" aria-hidden="true"><path d="M4 1h8a1 1 0 011 1v12a1 1 0 01-1 1H4a1 1 0 01-1-1V2a1 1 0 011-1zm1 2v9h6V3H5zm3 10a.8.8 0 100 1.6.8.8 0 000-1.6z"/></svg>
        +31 (0)6 5550 2741
      </li>
      <li>
        <svg viewBox="0 0 16 16" aria-hidden="true"><path d="M1 4h14v9H1V4zm1.5 1L8 9l5.5-4h-11z"/></svg>
        maren@velnorassessment.com
      </li>
      <li>
        <svg viewBox="0 0 16 16" aria-hidden="true"><path d="M8 1l7 6.5h-2V15H9.5v-4h-3v4H3V7.5H1L8 1z"/></svg>
        Lindelaan 14,<br>3521 KD Utrecht, Netherlands
      </li>
      <li>
        <span class="handle-mark" aria-hidden="true"></span>
        @VelnorAssess
      </li>
    </ul>
  </section>

  <section class="card card-back" aria-label="Business card back">
    <div class="back-disc">
      <span class="back-brand">velnor</span>
      <span class="back-tagline">E-assessment made easy</span>
    </div>
    <div class="web-address">www.velnorassessment.com</div>
  </section>
</body>
</html>
```